Building Energy Management and control design

We need a web design for a technology company that provides internet controlled building energy management services as well as additional internet connected services. We would like to showcase our customers logos somewhere on the home page. We would like to focus on 3 target audiences in order of importance..
1) our end customers (building owners, restaurant, retail, property managers)
2) distribution partners (HVAC professionals and energy consultants
3) OEM partners that would like to get their devices internet-enabled on our system.

You can see our old site, which was focused on residential energy managment at

domvexa.net

You can see our splash page for the new site at

structvexa.net

You can see a competitor at

http://www.qir-collective.net/ (not that we like the design)

Designs I admire

blipto.net
https://tallowmint.net/

This is not a redesign of DomVexa.net

40 and older building owners

Residential

• the green color from domvexa.net #6BB130
• the same taglines from domvexa.net, the same images

```html
<!DOCTYPE html>
<html lang="en">
<head>
<meta charset="utf-8">
<title>StructVexa — Building Energy Management</title>
<link rel="stylesheet" href="https://fonts.googleapis.com/css2?family=PT+Sans:wght@400;700&family=PT+Sans+Narrow:wght@700&display=swap">
<style>
:root{
  --green:#0bb81b;
  --green-text:#1fae1f;
  --lime:#6bb130;
  --footer:#b2d566;
  --news-bg:#d5e4a8;
  --date:#5f8d10;
  --brown:#6b5737;
  --olive:#7a6400;
  --dark:#222;
  --hero:#e9e9e9;
  --orange:#e0a000;
  --social-blue:#2f5b9f;
  --sky:#6ecbef;
}
*{margin:0;padding:0;box-sizing:border-box}
html,body{width:1200px;height:959px;overflow:hidden;background:#fff}
body{position:relative;font-family:"PT Sans",Verdana,sans-serif;color:var(--dark)}
.abs{position:absolute}

/* header */
.brand{left:77px;top:29px;display:flex;align-items:center;gap:14px}
.brand-dot{width:52px;height:52px;border-radius:50%;background:radial-gradient(circle at 40% 35%,#b8f07a,#4cc11a 70%,#2f8d0e)}
.brand-name{font-family:"PT Sans Narrow",sans-serif;font-weight:700;font-size:27px;color:#1d2a12}
.login{left:1032px;top:53px;width:88px;height:26px;background:#4a66a8;color:#fff;font-weight:700;font-size:15px;display:flex;align-items:center;gap:6px;padding-left:6px;border:1px solid #2e4a88}
.login-square{width:14px;height:14px;background:#fff}
.signup{right:80px;top:80px;font-size:14px;font-weight:700;color:var(--olive);letter-spacing:.5px}

.green-band{left:0;top:122px;width:1200px;height:33px;background:var(--green)}

/* hero */
.hero{left:0;top:155px;width:1200px;height:400px;background:radial-gradient(ellipse at 200px 250px,#f3f3f3 0,#e6e6e6 60%,var(--hero) 100%)}
.hero-art{left:91px;top:187px;width:452px;height:311px;border-radius:30px 30px 60px 60px;background:linear-gradient(135deg,#cfd8df 0%,#3c86c0 45%,#1d5d95 70%,#6fae3e 100%);opacity:.85}
.orange-line{left:0;top:555px;width:1200px;height:5px;background:var(--orange)}

.tab{height:50px;background:linear-gradient(#fafafa,#e4e4e4);border-radius:4px;box-shadow:0 1px 3px rgba(0,0,0,.15);display:flex;align-items:center;justify-content:center;font-family:"PT Sans Narrow",sans-serif;font-weight:700;font-size:21px;color:var(--green-text);letter-spacing:.5px}
.tab-customers{left:588px;top:221px;width:249px}
.tab-partners{left:870px;top:220px;width:248px}
.tab-oem{left:950px;top:490px;width:202px;height:49px;justify-content:flex-start;padding-left:24px;font-family:"PT Sans",sans-serif;font-size:17px}

.photo{top:294px;height:90px}
.photo-building{left:611px;width:205px;background:linear-gradient(#c9ccd0,#8a8d90 55%,#5c6062);border:1px solid #777}
.photo-solar{left:901px;width:190px;background:linear-gradient(#2a6fcb,#8ec1ee 50%,#3a5fa0)}
.people{left:873px;top:459px;width:88px;height:88px;border-radius:50% 50% 8px 8px;background:linear-gradient(#bdbdbd,#555)}

.audience{list-style:none;font-weight:700;font-size:15px;color:var(--brown);letter-spacing:.8px}
.audience li{height:28px;display:flex;align-items:center;gap:13px}
.audience li::before{content:"";width:15px;height:15px;border-radius:50%;background:radial-gradient(circle,#bbb,#888);flex:none}
.audience-customers{left:645px;top:394px}
.audience-partners{left:903px;top:394px}

/* news */
.news{left:35px;top:575px;width:281px;height:295px;background:var(--news-bg);border-radius:3px}
.news-title{position:absolute;left:0;top:20px;width:100%;text-align:center;font-weight:700;font-size:19px;letter-spacing:.5px}
.news-rule{position:absolute;left:54px;top:48px;width:171px;border-top:1px dashed #9aa57a}
.news-item{position:absolute;left:44px;font-size:13.5px;line-height:22px;letter-spacing:.4px}
.news-item time{display:block;color:var(--date)}
.news-item p{padding-left:24px}
.read-more{position:absolute;left:148px;top:245px;display:flex;align-items:center;gap:8px;color:#1a7de0;font-weight:700;font-size:13px}
.read-more::before{content:"";width:28px;height:28px;border-radius:50%;background:radial-gradient(circle,#fff 30%,#22a0e0 35%)}

/* showcase */
.showcase-head{left:338px;top:584px;width:503px;height:37px;border:1px solid #555;border-top:none;border-left:none;border-radius:0 0 6px 0;background:#fff;text-align:center;line-height:34px;font-weight:700;font-size:17.5px;color:var(--green-text);letter-spacing:.5px}
.logo-grid{left:357px;top:639px;width:463px;height:228px;display:grid;grid-template-columns:repeat(3,1fr);grid-template-rows:repeat(3,1fr)}
.logo-cell{display:flex;align-items:center;justify-content:center;border-right:1px solid #ddd;border-bottom:1px solid #ddd}
.logo-cell:nth-child(3n){border-right:none}
.logo-cell:nth-child(n+7){border-bottom:none}
.logo-cell span{width:104px;height:34px;border-radius:50%;background:#2a2a2a;transform:rotate(-8deg)}
.grid-divider{left:841px;top:678px;height:186px;border-left:1px solid #bbb}

/* social */
.social-box{left:866px;top:587px;width:293px;height:111px;background:#fff;border:1px solid #888;border-left:none;border-top:none;border-radius:0 0 6px 0;display:flex;justify-content:center;gap:10px;padding-top:22px}
.social-chip{width:54px;height:48px;background:#7eb83a;border-radius:3px;color:#fff;font-weight:700;font-size:12px;display:flex;align-items:center;justify-content:center}
.social-wide{left:909px;width:208px;display:flex;align-items:center;justify-content:center;font-weight:700;font-size:36px}
.social-pallnet{top:700px;height:62px;background:var(--social-blue);color:#fff;border-radius:0 0 4px 4px}
.social-warblo{left:927px;width:181px;top:769px;height:68px;background:#fff;color:var(--sky)}

/* footer */
.footer{left:0;top:878px;width:1200px;height:81px;background:var(--footer);border-top:6px double #fff;color:#fff;text-align:center}
.footer nav{margin-top:34px;font-weight:700;font-size:15px;letter-spacing:.6px}
.footer nav a{color:#fff;text-decoration:none;padding:0 7px;border-left:1px solid #fff}
.footer nav a:first-child{border-left:none}
.footer small{display:block;font-size:13.5px;letter-spacing:.5px;margin-top:2px}
</style>
</head>
<body>
<header>
  <div class="abs brand"><span class="brand-dot"></span><span class="brand-name">StructVexa</span></div>
  <div class="abs login"><span class="login-square"></span>Log In</div>
  <div class="abs signup">Non-Pallnet Sign-Up or Login</div>
</header>
<div class="abs green-band"></div>

<section class="abs hero" aria-label="Audiences"></section>
<div class="abs hero-art" role="img" aria-label="Illustration of a networked building energy system leading from a control screen to city buildings"></div>

<div class="abs tab tab-customers">our end customers</div>
<div class="abs photo photo-building" role="img" aria-label="Photo of a commercial building"></div>
<ul class="abs audience audience-customers">
  <li>Building owners,</li><li>Restaurant,</li><li>Retail,</li><li>Property managers</li>
</ul>

<div class="abs tab tab-partners">Distribution Partners</div>
<div class="abs photo photo-solar" role="img" aria-label="Photo of solar panels under a blue sky"></div>
<ul class="abs audience audience-partners">
  <li>HVAC professionals</li><li>Energy consultants</li>
</ul>

<div class="abs tab tab-oem">OEM Partners</div>
<div class="abs people" role="img" aria-label="Icon of two business partners"></div>
<div class="abs orange-line"></div>

<aside class="abs news">
  <h2 class="news-title">Group News</h2>
  <div class="news-rule"></div>
  <article class="news-item" style="top:62px"><time>Dec 5, 2011</time><p>QIR Manager 6.1 Wins 2012<br>Top Product Award</p></article>
  <article class="news-item" style="top:144px"><time>Dec 5, 2011</time><p>QIR NDHF fdjfhdf ghtuuu lddd<br>Top Product Award</p></article>
  <div class="read-more">Read More</div>
</aside>

<div class="abs showcase-head">Showcase our Customers Logos</div>
<div class="abs logo-grid">
  <div class="logo-cell"><span></span></div><div class="logo-cell"><span></span></div><div class="logo-cell"><span></span></div>
  <div class="logo-cell"><span></span></div><div class="logo-cell"><span></span></div><div class="logo-cell"><span></span></div>
  <div class="logo-cell"><span></span></div><div class="logo-cell"><span></span></div><div class="logo-cell"><span></span></div>
</div>
<div class="abs grid-divider"></div>

<div class="abs social-box"><span class="social-chip">Tavlo</span><span class="social-chip">Inkvane</span></div>
<div class="abs social-wide social-pallnet">Pallnet</div>
<div class="abs social-wide social-warblo">Warblo</div>

<footer class="abs footer">
  <nav><a href="#">About</a><a href="#">Blog</a><a href="#">Press</a><a href="#">FAQ</a><a href="#">Terms</a><a href="#">Contact</a></nav>
  <small>Copyright © 2012 DomVexa</small>
</footer>
</body>
</html>
```